E-commerce Website needs category banner

What we need for our category banner is a clean, predominately black design that showcases the product we are trying to sell (currently only 1), and a few subtle gradients that follow the pattern set by previous designs.

An example will be provided to showcase what we want.

It needs to say:
Outdoor Motion Detection Lighting in large, clear font similar to the example provided.

Please ensure dimensions are as follows: 980x300

Target Market(s)

Senior citizens, businesses, homeowners, families, etc

Industry/Entity Type

Product

Font styles to use
Sans Serif

Requirements
Must have
• It needs to say:
Outdoor Motion Detection Lighting in large, clear font similar to the example provided
980x300 is the required size!
Should not have
• Too much going on- clean and simple please (no crazy fonts, logos, etc)

```html
<!DOCTYPE html>
<html lang="en">
<head>
<meta charset="utf-8">
<title>Outdoor Motion Detection Lighting</title>
<link rel="stylesheet" href="https://fonts.googleapis.com/css2?family=Archivo+Black&display=swap">
<style>
  :root {
    --bg-center: #3a3a3a;
    --bg-mid: #262626;
    --bg-edge: #121212;
    --headline: #ffffff;
    --product-light: #e4e4e4;
    --product-shade: #a9a9a9;
  }
  html, body {
    margin: 0;
    padding: 0;
    overflow: hidden;
    background: var(--bg-edge);
  }
  .banner {
    position: relative;
    width: 1200px;
    height: 367px;
    overflow: hidden;
    background:
      radial-gradient(ellipse 70% 95% at 58% 40%, var(--bg-center) 0%, var(--bg-mid) 45%, var(--bg-edge) 100%);
  }
  .banner::after {
    content: "";
    position: absolute;
    inset: 0;
    background:
      repeating-linear-gradient(45deg, rgba(255,255,255,0.025) 0 1px, transparent 1px 4px),
      repeating-linear-gradient(-45deg, rgba(0,0,0,0.08) 0 1px, transparent 1px 4px);
    pointer-events: none;
  }
  .headline {
    position: absolute;
    left: 124px;
    top: 44px;
    margin: 0;
    font-family: "Archivo Black", "Arial Black", sans-serif;
    font-size: 73px;
    line-height: 66px;
    letter-spacing: 1px;
    color: var(--headline);
    text-transform: uppercase;
    z-index: 1;
  }
  .product-visual {
    position: absolute;
    left: 725px;
    top: 28px;
    width: 400px;
    height: 300px;
    border-radius: 46% 50% 40% 44%;
    background:
      radial-gradient(ellipse at 35% 30%, var(--product-light) 0%, var(--product-shade) 60%, rgba(169,169,169,0) 78%);
    opacity: 0.85;
    z-index: 1;
  }
</style>
</head>
<body>
  <main class="banner">
    <h1 class="headline">Outdoor<br>Motion<br>Detection<br>Lighting</h1>
    <div class="product-visual" role="img" aria-label="Two white wall-mounted battery LED motion sensor spotlights on swivel brackets"></div>
  </main>
</body>
</html>
```